Window Decal for Speech, Feeding, Occupational, Physical, and Behavior Therapy office for children

I need a high resolution, vertical design, preferably via Adobe Illustrator (real size design) that can be applied to office store front windows, in the form of window decals. The business is called Bright Steps Therapy and we provide Speech, Feeding, Occupational, Physical and Behavior Therapy for children; therefore, the design must be relay a kid-friendly image, while highlighting conditions we treat/service. We are looking to apply signage to (4) glass windows and (1) glass entry door. I have uploaded (3) attachments - a draft design (with window measurements), our company logo and an image of the store front.

Target Market(s)

Parents

Industry/Entity Type

Healthcare

Colors

Designer to choose colors to be used in the design.

Requirements
Must have
• Imagery must be high resolution
• The logo is trademarked, so it must stay the same.
• The (3) window design of the faces blowing bubbles, with the depicted wording is necessary; however, the imagery and layout can both be improved upon, yet I still need a resemblance to what is provided. Additionally, I've added (2) new facial images from the interior walls of our clinic. My preference is to have the faces for the exterior windows mirror these images as closely as possible in terms of skin tone (darkness), definition and realism.
• Also, please provide bleed room along the edges in your design.

```html
<!DOCTYPE html>
<html lang="en">
<head>
<meta charset="utf-8">
<title>Bright Steps Therapy – Window Decals</title>
<link href="https://fonts.googleapis.com/css2?family=Bebas+Neue&family=Source+Sans+3:wght@400;600;700&display=swap" rel="stylesheet">
<style>
  :root{
    --page:#ffffff;
    --frame:#f7941d;
    --silver-dark:#b9b9bb;
    --silver-mid:#d6d6d8;
    --silver-light:#f7f7f8;
    --ink:#231f20;
    --brand:#2b2a5c;
    --speech:#00a651;
    --feeding:#0072bc;
    --occupational:#662d91;
    --grass-light:#8cc63f;
    --grass-dark:#3d8b37;
  }
  *{box-sizing:border-box;margin:0;padding:0}
  html,body{width:1200px;height:849px;overflow:hidden;background:var(--page)}
  body{position:relative;font-family:"Source Sans 3",sans-serif;color:var(--ink)}

  .decal{
    position:absolute;
    border:1.5px solid var(--frame);
    background:linear-gradient(90deg,
      var(--silver-dark) 0%,var(--silver-light) 18%,var(--silver-mid) 40%,
      var(--silver-dark) 55%,var(--silver-light) 75%,var(--silver-mid) 90%,var(--silver-dark) 100%);
    text-align:center;
    overflow:hidden;
  }
  .decal--door{left:78px;top:304px;width:131px;height:288px}
  .decal--tall{left:230px;top:182px;width:164px;height:410px}
  .decal--wide{left:417px;top:182px;width:692px;height:410px;
    background:
      linear-gradient(90deg,var(--silver-dark) 0%,var(--silver-light) 12%,var(--silver-mid) 25%,var(--silver-dark) 33.3%,
      var(--silver-light) 45%,var(--silver-mid) 58%,var(--silver-dark) 66.6%,var(--silver-light) 78%,var(--silver-mid) 90%,var(--silver-dark) 100%);}

  .brand-name{font-weight:600;color:var(--brand);line-height:1.05;display:flex;align-items:center;justify-content:center;gap:5px}
  .brand-dot{width:10px;height:10px;border-radius:50%;background:var(--speech);flex:none}

  .decal--door .brand-name{position:absolute;top:48px;left:0;right:0;font-size:15px}
  .door-motto{position:absolute;top:126px;left:0;right:0;font-size:6px;font-weight:700;font-style:normal}
  .door-hours{position:absolute;top:143px;left:0;right:0;font-size:6.5px;font-weight:700;line-height:1.4}
  .door-follow{position:absolute;top:168px;left:0;right:0;font-size:8px;font-weight:700}

  .decal--tall .brand-name{position:absolute;top:78px;left:6px;right:6px;font-size:20px}
  .tagline{position:absolute;top:160px;left:0;right:0;font-size:9px;font-weight:700}
  .service-band{position:absolute;top:185px;left:1px;right:1px;display:flex;height:13px;font-size:9px;font-weight:700;color:#fff;line-height:13px}
  .service-band span{flex:1}
  .service-band .speech{background:var(--speech);flex:.75}
  .service-band .feeding{background:var(--feeding);flex:.75}
  .service-band .occupational{background:var(--occupational);flex:1.2}
  .more-services{position:absolute;top:211px;left:0;right:0;font-size:10px;font-weight:700;line-height:1.3}
  .reassurance{position:absolute;top:274px;left:0;right:0;font-size:14px;font-weight:700}

  .window-art{position:absolute;inset:0;width:100%;height:100%}
  .cloud-label{font-family:"Bebas Neue",sans-serif;fill:#fff;text-anchor:middle;letter-spacing:.5px}
  .pane-divider{stroke:var(--frame);stroke-width:1.5}
</style>
</head>
<body>

<section class="decal decal--door" aria-label="Entry door decal">
  <div class="brand-name"><span class="brand-dot"></span>Bright Steps Therapy</div>
  <p class="door-motto">“…where serving you is therapeutic!”</p>
  <p class="door-hours">Hours: 9 a.m. – 8 p.m.<br>Phone: 555-014-2270</p>
  <p class="door-follow">Follow @brightstepsclinic</p>
</section>

<section class="decal decal--tall" aria-label="Single window decal">
  <div class="brand-name"><span class="brand-dot"></span>Bright Steps Therapy</div>
  <p class="tagline">“Getting Our Kids Back on Track”</p>
  <div class="service-band">
    <span class="speech">Speech</span><span class="feeding">Feeding</span><span class="occupational">Occupational</span>
  </div>
  <p class="more-services">Applied Behavior Analysis<br>Physical Therapy</p>
  <p class="reassurance">“You Are Not Alone.”</p>
</section>

<section class="decal decal--wide" aria-label="Three-pane window decal">
  <svg class="window-art" viewBox="0 0 692 410" xmlns="http://www.w3.org/2000/svg">
    <defs>
      <symbol id="cloud-shape" viewBox="0 0 100 60" preserveAspectRatio="none">
        <path d="M20,57 C4,57 0,40 10,33 C4,17 22,7 32,14 C38,1 62,0 68,11 C80,4 96,14 91,28 C100,35 98,57 82,57 Z"
              stroke="#fff" stroke-width="2.5" vector-effect="non-scaling-stroke"/>
      </symbol>
      <linearGradient id="hill-tone" x1="0" y1="0" x2="0" y2="1">
        <stop offset="0" stop-color="var(--grass-light)"/>
        <stop offset="1" stop-color="var(--grass-dark)"/>
      </linearGradient>
    </defs>

    <path role="img" aria-label="Illustration: grassy hill with trees, a rainbow, a smiling sun, a seesaw and two children playing"
          d="M0,410 L0,345 Q30,300 80,300 Q200,290 330,300 Q470,300 560,320 Q650,335 692,370 L692,410 Z"
          fill="url(#hill-tone)"/>

    <line class="pane-divider" x1="230.5" y1="0" x2="230.5" y2="410"/>
    <line class="pane-divider" x1="461.5" y1="0" x2="461.5" y2="410"/>

    <g class="condition-clouds">
      <use href="#cloud-shape" x="13" y="10" width="90" height="52" fill="#29abe2"/>
      <text class="cloud-label" x="58" y="33" font-size="17">PICKY</text>
      <text class="cloud-label" x="58" y="52" font-size="17">EATER</text>

      <use href="#cloud-shape" x="119" y="29" width="100" height="56" fill="#8dc63f"/>
      <text class="cloud-label" x="169" y="64" font-size="17">ARTICULATION</text>

      <use href="#cloud-shape" x="35" y="74" width="64" height="36" fill="#1fa99c"/>
      <text class="cloud-label" x="67" y="99" font-size="16">AUTISM</text>

      <use href="#cloud-shape" x="133" y="104" width="80" height="56" fill="#662d91"/>
      <text class="cloud-label" x="173" y="131" font-size="17">SPEECH</text>
      <text class="cloud-label" x="173" y="150" font-size="17">DELAY</text>

      <use href="#cloud-shape" x="13" y="145" width="80" height="52" fill="#f15a29"/>
      <text class="cloud-label" x="53" y="170" font-size="17">VOICE</text>
      <text class="cloud-label" x="53" y="190" font-size="17">DISORDER</text>

      <use href="#cloud-shape" x="118" y="182" width="80" height="48" fill="#ec2079"/>
      <text class="cloud-label" x="158" y="214" font-size="17">STUTTERING</text>

      <use href="#cloud-shape" x="248" y="36" width="192" height="116" fill="#00a651"/>
      <text class="cloud-label" x="344" y="85" font-size="14">IS YOUR CHILD</text>
      <text class="cloud-label" x="344" y="102" font-size="14">ON TRACK?</text>
      <text class="cloud-label" x="344" y="136" font-size="14">EARLY INTERVENTION MATTERS</text>

      <use href="#cloud-shape" x="518" y="15" width="120" height="72" fill="#9e1f63"/>
      <text class="cloud-label" x="578" y="44" font-size="14">BALANCE</text>
      <text class="cloud-label" x="578" y="61" font-size="14">&amp;</text>
      <text class="cloud-label" x="578" y="78" font-size="14">COORDINATION</text>

      <use href="#cloud-shape" x="467" y="103" width="92" height="56" fill="#2e3192"/>
      <text class="cloud-label" x="513" y="129" font-size="14">SOCIAL</text>
      <text class="cloud-label" x="513" y="147" font-size="14">SKILLS</text>

      <use href="#cloud-shape" x="575" y="144" width="92" height="52" fill="#f7941d"/>
      <text class="cloud-label" x="621" y="167" font-size="14">TOE</text>
      <text class="cloud-label" x="621" y="184" font-size="14">WALKING</text>
    </g>
  </svg>
</section>

</body>
</html>
```